Keystone Prime Water Tank

I primarily market the water tanks so want a business care that reflects that. I have attached the water tank logo. You have been working on our water tank so maybe we can use that on the card et. I am leaving as one sided but can be double sided if that works. The information that needs to be on the cards is as follows: Gerald T. Munro Phone numbers: Office 555-284-9137 Direct 555-619-2405 Mobile 555-372-5841 email address: gerald@fieldgearworks.com Address P.O. Box 8273 Windermere, FL 30512 Web Page: www.fieldgearworks.com. A lot to fit on the card. Thanks

```html
<!DOCTYPE html>
<html lang="en">
<head>
<meta charset="UTF-8">
<title>Keystone Prime Water Tank – Business Card</title>
<link rel="stylesheet" href="https://fonts.googleapis.com/css2?family=Archivo:wght@700;800&family=Arimo:wght@400;700&display=swap">
<style>
  :root {
    --ink: #1e1e1f;
    --red: #e8070e;
    --white: #ffffff;
    --paper: #ececec;
    --text: #1a1a1a;
  }
  * { box-sizing: border-box; margin: 0; padding: 0; }
  html, body { width: 1200px; height: 900px; overflow: hidden; }
  body {
    background: var(--paper);
    font-family: "Arimo", Arial, sans-serif;
    position: relative;
  }
  .card {
    position: absolute;
    left: 250px;
    width: 700px;
    height: 400px;
    overflow: hidden;
    box-shadow: 0 6px 18px rgba(0,0,0,0.18);
  }
  .card--back { top: 30px; background: var(--ink); }
  .card--front { top: 470px; background: var(--white); }

  .card__waves { position: absolute; inset: 0; width: 100%; height: 100%; }

  /* brand lockup */
  .brand {
    position: absolute;
    display: flex;
    align-items: center;
    gap: 14px;
  }
  .brand__mark { background: var(--red); flex: none; }
  .brand__name {
    font-family: "Arimo", Arial, sans-serif;
    font-weight: 700;
    text-transform: uppercase;
    line-height: 1.08;
    letter-spacing: 0.5px;
    white-space: nowrap;
  }
  .card--back .brand {
    left: 50%; top: 50%;
    transform: translate(-50%, -50%);
  }
  .card--back .brand__mark { width: 62px; height: 62px; }
  .card--back .brand__name { color: var(--white); font-size: 32px; }

  .card--front .brand { right: 40px; top: 70px; gap: 12px; }
  .card--front .brand__mark { width: 46px; height: 46px; }
  .card--front .brand__name { color: var(--text); font-size: 22px; }

  /* contact block */
  .holder {
    position: absolute;
    left: 70px; top: 46px;
    font-family: "Archivo", Arial, sans-serif;
    font-weight: 800;
    font-size: 27px;
    color: var(--red);
    letter-spacing: 1px;
    text-transform: uppercase;
    white-space: nowrap;
  }
  .address {
    position: absolute;
    left: 78px; top: 104px;
    font-size: 17px;
    line-height: 22px;
    color: var(--text);
    font-style: normal;
  }
  .contacts {
    position: absolute;
    left: 78px; top: 164px;
    list-style: none;
    font-size: 18px;
    color: var(--text);
  }
  .contacts__item {
    display: flex;
    align-items: center;
    gap: 10px;
    height: 25px;
    white-space: nowrap;
  }
  .contacts__icon { width: 16px; height: 16px; flex: none; }
  .contacts__label { color: var(--red); margin-left: 4px; }

  .website {
    position: absolute;
    right: 38px; bottom: 34px;
    font-size: 16px;
    color: var(--red);
  }
</style>
</head>
<body>

  <section class="card card--back" aria-label="Card back">
    <div class="brand">
      <span class="brand__mark"></span>
      <span class="brand__name">Keystone Prime<br>Water Tank</span>
    </div>
  </section>

  <section class="card card--front" aria-label="Card front">
    <svg class="card__waves" viewBox="0 0 700 400" preserveAspectRatio="none" aria-hidden="true">
      <path d="M0,306 C170,334 330,306 470,232 C340,312 170,342 0,332 Z" fill="var(--red)"/>
      <path d="M0,342 C210,354 410,322 540,242 C610,198 660,176 700,166 L700,400 L0,400 Z" fill="var(--ink)"/>
    </svg>

    <h1 class="holder">Gerald T. Munro</h1>

    <address class="address">
      P.O. Box 8273 Larkfield<br>FL 30512
    </address>

    <ul class="contacts">
      <li class="contacts__item">
        <svg class="contacts__icon" viewBox="0 0 16 16"><path d="M3 1.5 L6 1 L7 5 L5 6.2 C6 8.5 7.5 10 9.8 11 L11 9 L15 10 L14.5 13 C14 14.5 12 15 10 14 C6 12.5 3.5 10 2 6 C1 4 1.5 2.2 3 1.5 Z" fill="var(--red)"/></svg>
        <span>555-284-9137<span class="contacts__label">(OFFICE)</span></span>
      </li>
      <li class="contacts__item">
        <svg class="contacts__icon" viewBox="0 0 16 16"><path d="M3 1.5 L6 1 L7 5 L5 6.2 C6 8.5 7.5 10 9.8 11 L11 9 L15 10 L14.5 13 C14 14.5 12 15 10 14 C6 12.5 3.5 10 2 6 C1 4 1.5 2.2 3 1.5 Z" fill="var(--red)"/></svg>
        <span>555-619-2405<span class="contacts__label">(DIRECT)</span></span>
      </li>
      <li class="contacts__item">
        <svg class="contacts__icon" viewBox="0 0 16 16"><rect x="3.5" y="1" width="9" height="14" rx="1.5" fill="none" stroke="var(--red)" stroke-width="1.6"/><circle cx="8" cy="12.5" r="0.9" fill="var(--red)"/></svg>
        <span>555-372-5841</span>
      </li>
      <li class="contacts__item">
        <svg class="contacts__icon" viewBox="0 0 16 16"><rect x="1" y="3" width="14" height="10" fill="var(--red)"/><path d="M1 3 L8 9 L15 3" fill="none" stroke="var(--white)" stroke-width="1.2"/></svg>
        <span>gerald@fieldgearworks.com</span>
      </li>
    </ul>

    <div class="brand">
      <span class="brand__mark"></span>
      <span class="brand__name">Keystone Prime<br>Water Tank</span>
    </div>

    <p class="website">www.fieldgearworks.com</p>
  </section>

</body>
</html>
```